Vocational Mentor needs an impressive business card

1. I need a business card (or maybe three with identic look) to promote me and my three business titles/services:
- Vocational Mentor. I help people find their vocation and live happily from it. I use my 20 years of experience in business, management and psychology to help them identify the most efficient ways to make a living doing what they are passionate about.
- Business Angel. I help founders start a succesful business with minimum risks and costs. I use my 20 years of experience in sales, management and entrepreneurship to help them identify the most efficient ways, in terms of time and cost, to validate their business idea.
- Learning Designer. I design unique learning programs that produce long-term cognitive and behavioural changes to people and organisations. I use my 20 years of experience in learning, teaching and change management to create minimalist experiences and processes that allow them to change efficiently in their pursued direction.

2. I would like a two-sided business card, on the front with my name, contact details and titles, on the back the explanation of the services.
Updates

Hi all,

I updated my brief, included contacts info and give feedback on all designs I got. I am new on this platform so please tell me if you need anything else or if I don't use corectly the platform forms.

Kind regards,
Tudor

Hi all,

I shortened the services description by deleting the phrase "I call..."

Kind regards,
Tudor

Target Market(s)

Freelancers, startups, people and organization willing to invest in change through ultimate learning experiences

Industry/Entity Type

Business

Font styles to use
Serif

Requirements
Must have
• Front side: full name, titles, web site, email, phone like below:
Tudor Vasilache
Vocational Mentor, Business Angel, Learning Designer
info@tudorvasilache.example
www.tudorvasilache.example
+40-745-TUDORV
Nice to have
• Back side: the description of the services I provide as in the task description.
1/3: it would be nice if I can jam all three titles on the front side but then I need a solution to jam all three services on the back side.

```html
<!DOCTYPE html>
<html lang="en">
<head>
<meta charset="utf-8">
<title>Tudor Vasilache – Business Card</title>
<link rel="stylesheet" href="https://fonts.googleapis.com/css2?family=Open+Sans:wght@300;400;700&display=swap">
<style>
  :root {
    --backdrop: #3a3a3a;
    --card-front: #0c0c0d;
    --card-back: #1f1d1d;
    --name-grey: #3e4346;
    --title-grey: #6f7b82;
    --contact-grey: #8a969c;
    --heading-cyan: #6fd3ee;
    --body-teal: #3f8ea3;
    --smoke-light: rgba(120, 160, 170, 0.35);
    --smoke-dark: rgba(40, 60, 66, 0);
  }
  * { margin: 0; padding: 0; box-sizing: border-box; }
  html, body { width: 1200px; height: 750px; overflow: hidden; }
  body {
    background: radial-gradient(ellipse at 50% 40%, #4a4a4a 0%, var(--backdrop) 60%, #262626 100%);
    font-family: "Open Sans", sans-serif;
    position: relative;
  }
  .card {
    position: absolute;
    top: 218px;
    width: 540px;
    height: 314px;
    overflow: hidden;
    box-shadow: 0 12px 30px rgba(0, 0, 0, 0.55);
  }
  .card--front { left: 40px; background: var(--card-front); }
  .card--back { left: 620px; background: var(--card-back); }

  .smoke {
    position: absolute;
    border-radius: 50%;
    background: radial-gradient(ellipse at center, var(--smoke-light) 0%, var(--smoke-dark) 70%);
  }
  .card--front .smoke { left: 60px; top: 40px; width: 400px; height: 150px; transform: rotate(-28deg); top: 90px; }
  .card--back .smoke { left: -40px; top: 40px; width: 180px; height: 320px; transform: rotate(10deg); opacity: 0.6; }

  .front-content {
    position: absolute;
    left: 190px;
    top: 86px;
    width: 220px;
    text-align: center;
  }
  .name {
    font-weight: 700;
    font-size: 20px;
    color: var(--name-grey);
    text-shadow: 0 1px 0 #8a9398, 0 -1px 0 #000;
    letter-spacing: 0.3px;
  }
  .titles {
    margin-top: 6px;
    font-weight: 300;
    font-size: 16px;
    line-height: 19px;
    color: var(--title-grey);
  }
  .contacts {
    list-style: none;
    margin-top: 24px;
    font-size: 12px;
    line-height: 16px;
    color: var(--contact-grey);
    font-weight: 300;
    display: inline-block;
    text-align: left;
  }
  .contacts li { display: flex; align-items: center; gap: 7px; }
  .contacts svg { width: 10px; height: 10px; flex: none; }

  .services {
    position: absolute;
    left: 48px;
    top: 32px;
    right: 34px;
  }
  .service + .service { margin-top: 12px; }
  .service-title {
    font-weight: 700;
    font-size: 11.5px;
    color: var(--heading-cyan);
    margin-bottom: 4px;
  }
  .service-text {
    font-size: 10px;
    line-height: 12.5px;
    color: var(--body-teal);
  }
</style>
</head>
<body>
  <section class="card card--front">
    <div class="smoke" role="img" aria-label="Soft teal smoke swirl flowing diagonally across the card"></div>
    <div class="front-content">
      <h1 class="name">Tudor Vasilache</h1>
      <p class="titles">Vocational Mentor<br>Business Angel<br>Learning Designer</p>
      <ul class="contacts">
        <li>
          <svg viewBox="0 0 10 10" fill="none" stroke="currentColor" stroke-width="1"><rect x="0.5" y="2" width="9" height="6.5"/><path d="M0.5 2 L5 6 L9.5 2"/></svg>
          office@tudorvasilache.example
        </li>
        <li>
          <svg viewBox="0 0 10 10" fill="none" stroke="currentColor" stroke-width="1"><circle cx="5" cy="5" r="4.3"/><ellipse cx="5" cy="5" rx="1.8" ry="4.3"/><path d="M0.7 5 H9.3"/></svg>
          www.tudorvasilache.example
        </li>
        <li>
          <svg viewBox="0 0 10 10" fill="currentColor"><path d="M2 1 L3.6 1 L4.2 3 L3 3.8 Q4 6 6.2 7 L7 5.8 L9 6.4 L9 8 Q8.5 9 7.5 9 Q1 8 1 2.5 Q1 1.3 2 1 Z"/></svg>
          0040 745 000
        </li>
      </ul>
    </div>
  </section>

  <section class="card card--back">
    <div class="smoke" role="img" aria-label="Faint teal smoke swirl along the left edge"></div>
    <div class="services">
      <article class="service">
        <h2 class="service-title">Vocational Mentor</h2>
        <p class="service-text">I help people to find their vocation and live happily from it. I use my 20 years of experience in business, management and psychology to help them identify the most efficient ways to make a living doing what they are passionate about. I call this service vocational mentoring.</p>
      </article>
      <article class="service">
        <h2 class="service-title">Business Angel</h2>
        <p class="service-text">I help founders to start a succesful business with minimum risks and costs. I use my 20 years of experience in sales, management and entrepreneurship to help them identify the most efficient ways, in terms of time and cost, to validate their business idea. I call this service lean-startup mentoring.</p>
      </article>
      <article class="service">
        <h2 class="service-title">Learning Designer</h2>
        <p class="service-text">I design unique learning programs that produce long-term cognitive and behavioural changes to people and organisations. I use my 20 years of experience in learning, teaching and change management to create minimalist experiences and processes that allows them to change efficiently in their pursued direction. I call this service ultimate learning design.</p>
      </article>
    </div>
  </section>
</body>
</html>
```